Corporate Identity Pack - LetterHead, Business Card, Envelope

We are looking for a clean, professional, and visually connected corporate identity set for our company "VELTA HOME" (Cleaning, Gardening, and Pest Control services).

The pack must include:

Business Card (front and back)
Envelope with recipient window on the right side (22x11)
A4 Letterhead

We provide:
Our final logo (PNG)
Three design references (Inspiration1, Inspiration2, Inspiration3) to spark ideas — but you are absolutely free to propose your own creative solutions based on these concepts.

What we want:
A clean, modern, and trustworthy style
A subtle but creative watermark or graphic detail on the letterhead (not too invasive)

The same visual "family feeling" across business card, envelope, and letterhead: designs must be different but clearly connected

Strong readability for all text and contact details

Use our brand colors (Navy Blue, Green, Orange/Red) in a smart, non-overloaded way

No strict limitations: we are open to creative proposals as long as they are coherent, elegant, and suitable for professional use

Technical specifications:
100% full A4 page layout (no accidental borders)

Deliver ready-to-print PDFs and vector files (AI, EPS)

Respect 5 mm safety margins

Standard sizes for A4, business card, envelope C6 with window at the right

Tone:
Modern – Clean – Elegant – Creative – Trustworthy

Target Market(s)

Professional businesses, property managers, condominium administrators, companies, clinics, and offices requiring cleaning, gardening, and pest control services. The design must convey trust, reliability, professionalism, and attention to detail.

Industry/Entity Type

Cleaning Services, Gardening Services, Pest Control Services

Colors
0054AA
0677BA
7BADD7
CADEEF
E8F1F8
59FF00
82FF00
B8FF75
E3FFCB
F4FFEA
EB3D1F
EC4F4E
F09395
F8D3D4
FCEDEE

Requirements
Must have
• Cohesive design across business card, letterhead, and envelope Clean, modern, professional look Use of brand colors: Navy Blue (main), Green, Orange/Red accents Letterhead must include a subtle watermark without interfering with text Envelope must be with a transparent window for recipient address visibility High readability of all text and contact details Proper alignment, no unnecessary margins (full A4 layout)
Nice to have
• Creative but discreet use of the checkmark from the logo as part of the background or watermark Slight variation or accent of color tones while respecting brand identity A clean visual accent that gives a sense of movement or dynamic professionalism (without being distracting) Icons for email, phone, and website on the business card (if stylistically appropriate)
Should not have
• Overuse of colors or rainbow effects Heavy backgrounds or complex textures that interfere with readability Fonts that are too playful, comic-style, or non-professional Overcrowded layouts — the design must feel clean and spacious Watermarks that are too strong or central (they must be subtle and marginal)

```html
<!DOCTYPE html>
<html lang="en">
<head>
<meta charset="utf-8">
<title>Velta Home – Stationery Set</title>
<link href="https://fonts.googleapis.com/css2?family=Arimo:wght@400;700&display=swap" rel="stylesheet">
<style>
:root{
  --navy:#0d0a72;
  --green:#6ccb2f;
  --orange:#ff6600;
  --ink:#1e1e24;
  --paper:#ffffff;
  --stage:#605c5b;
  --wm-navy:#f0f0f7;
  --wm-green:#f5faf1;
}
*{margin:0;padding:0;box-sizing:border-box}
html,body{width:1200px;height:866px;overflow:hidden;background:var(--stage)}
body{position:relative;font-family:"Arimo",Arial,sans-serif;color:var(--ink)}
.sheet{position:absolute;background:var(--paper);box-shadow:6px 7px 8px rgba(0,0,0,.45);overflow:hidden}
.abs{position:absolute}
.bars{position:absolute;left:0;top:0}
.brand{position:absolute;display:flex;align-items:center;font-weight:700;color:var(--navy);white-space:nowrap;letter-spacing:.02em}
.brand .dot{background:var(--navy);flex:none}
.services{position:absolute;color:var(--navy);font-weight:400;letter-spacing:.08em;white-space:nowrap}
.line{position:absolute;white-space:nowrap;display:flex;align-items:center}
.ico{flex:none;display:inline-flex;align-items:center;justify-content:center}
.watermark{position:absolute;background:linear-gradient(135deg,var(--wm-navy) 0%,var(--wm-navy) 45%,var(--wm-green) 100%)}

/* business card 1 */
.card-a{left:158px;top:48px;width:224px;height:131px}
.card-a .brand{left:46px;top:12px;font-size:15px}
.card-a .brand .dot{width:16px;height:16px;margin-right:6px}
.card-a .services{left:68px;top:33px;font-size:6px}
.card-a .line{left:14px;font-size:5.6px}
.card-a .on-navy{color:#fff}

/* business card 2 */
.card-b{left:125px;top:225px;width:224px;height:131px}
.card-b .brand{left:44px;top:12px;font-size:15px}
.card-b .brand .dot{width:16px;height:16px;margin-right:6px}
.card-b .services{left:66px;top:33px;font-size:6px}
.card-b .line{font-size:5.8px}
.card-b .divider{position:absolute;left:112px;top:62px;width:1px;height:44px;background:var(--navy)}

/* business card 3 */
.card-c{left:390px;top:192px;width:224px;height:131px}
.card-c .brand{left:53px;top:14px;font-size:13px}
.card-c .brand .dot{width:11px;height:11px;margin-right:5px}
.card-c .company{position:absolute;left:0;width:224px;text-align:center;font-weight:700;font-size:6.6px;color:var(--ink)}
.card-c .line{left:11px;font-size:5.8px}
.card-c .on-navy{color:#fff}

/* envelope */
.envelope{left:34px;top:435px;width:582px;height:271px}
.envelope .brand{left:32px;top:33px;font-size:25px}
.envelope .brand .dot{width:22px;height:22px;margin-right:10px}
.envelope .watermark{left:220px;top:30px;width:214px;height:195px}
.envelope .line{left:65px;font-size:9.6px;color:var(--ink)}

/* letterhead */
.letterhead{left:652px;top:114px;width:513px;height:725px}
.letterhead .head-brand{left:32px;top:40px;font-size:22px}
.letterhead .head-brand .dot{width:24px;height:24px;margin-right:10px}
.letterhead .services{left:68px;top:64px;font-size:6.4px}
.letterhead .contact{left:360px;font-size:9.6px}
.letterhead .contact .ico{width:18px;margin-right:8px}
.letterhead .watermark{left:67px;top:185px;width:378px;height:395px;opacity:.75}
.letterhead .to{position:absolute;left:83px;top:134px;font-size:9.2px}
.letterhead .to strong{display:block;font-size:10px;margin-top:2px}
.letterhead .body{position:absolute;left:82px;width:378px;font-size:6.6px;line-height:10.2px;color:#2a2a30}
.letterhead .sign{position:absolute;right:58px;top:568px;text-align:right;font-size:9.6px;line-height:12px}
.letterhead .sign strong{display:block}
.letterhead .foot-brand{left:18px;top:670px;font-size:13px}
.letterhead .foot-brand .dot{width:14px;height:14px;margin-right:6px}
.letterhead .foot{top:670px;font-size:9.6px}
</style>
</head>
<body>

<!-- business card: contact front -->
<section class="sheet card-a" aria-label="Business card front">
  <svg class="bars" width="224" height="131" viewBox="0 0 224 131" aria-hidden="true">
    <rect x="0" y="73" width="155" height="32" fill="var(--navy)"/>
    <rect x="160" y="61" width="51" height="52" fill="var(--navy)"/>
    <rect x="216" y="73" width="8" height="32" fill="var(--navy)"/>
  </svg>
  <div class="brand"><span class="dot"></span>VELTA HOME</div>
  <div class="services">CLEANING · GARDENING · PESTCONTROL</div>
  <div class="line on-navy" style="top:78px"><span class="ico" style="width:10px">
    <svg width="5" height="5" viewBox="0 0 10 10"><path d="M2 0l2 2-1 2 3 3 2-1 2 2-2 2C4 10 0 6 0 2z" fill="#fff"/></svg></span>&nbsp;+39 331 5208147</div>
  <div class="line on-navy" style="top:87px"><span class="ico" style="width:10px;font-weight:700">@</span>&nbsp;office@velta-home.srl</div>
  <div class="line on-navy" style="top:96px"><span class="ico" style="width:10px">
    <svg width="5" height="5" viewBox="0 0 10 10"><circle cx="5" cy="5" r="4.3" fill="none" stroke="#fff"/><path d="M1 5h8M5 1v8" stroke="#fff" stroke-width=".8"/></svg></span>&nbsp;www.velta-home.srl</div>
  <div class="line" style="top:106px"><span class="ico" style="width:10px">
    <svg width="8" height="4" viewBox="0 0 16 8"><rect x=".5" y=".5" width="15" height="7" rx="3.5" fill="none" stroke="var(--navy)"/></svg></span>&nbsp;info.veltahome@pec.it</div>
  <div class="line" style="top:115px"><span class="ico" style="width:10px">
    <svg width="4" height="5" viewBox="0 0 8 10"><rect x=".5" y=".5" width="7" height="9" fill="none" stroke="var(--navy)"/><path d="M2 4h4M2 6h4" stroke="var(--navy)"/></svg></span>&nbsp;K7QWT42</div>
</section>

<!-- business card: brand front -->
<section class="sheet card-b" aria-label="Business card alternate">
  <svg class="bars" width="224" height="131" viewBox="0 0 224 131" aria-hidden="true">
    <rect x="0" y="70" width="25" height="6" rx="3" fill="var(--navy)"/>
    <rect x="0" y="80" width="25" height="6" rx="3" fill="var(--navy)"/>
    <rect x="0" y="89" width="25" height="6" rx="3" fill="var(--navy)"/>
    <polygon points="0,116 174,116 171,121 0,121" fill="var(--orange)"/>
    <polygon points="178,116 194,116 191,121 175,121" fill="var(--navy)"/>
    <polygon points="199,116 224,116 224,121 196,121" fill="var(--green)"/>
  </svg>
  <div class="brand"><span class="dot"></span>VELTA HOME</div>
  <div class="services">CLEANING · GARDENING · PESTCONTROL</div>
  <div class="line" style="left:29px;top:70px">+39 331 5208147</div>
  <div class="line" style="left:29px;top:80px">office@velta-home.srl</div>
  <div class="line" style="left:29px;top:89px">www.velta-home.srl</div>
  <div class="divider"></div>
  <div class="line" style="left:144px;top:73px"><span class="ico" style="width:10px">
    <svg width="8" height="4" viewBox="0 0 16 8"><rect x=".5" y=".5" width="15" height="7" rx="3.5" fill="none" stroke="var(--navy)"/></svg></span>&nbsp;info.veltahome@pec.it</div>
  <div class="line" style="left:144px;top:83px"><span class="ico" style="width:10px">
    <svg width="4" height="5" viewBox="0 0 8 10"><rect x=".5" y=".5" width="7" height="9" fill="none" stroke="var(--navy)"/><path d="M2 4h4M2 6h4" stroke="var(--navy)"/></svg></span>&nbsp;K7QWT42</div>
</section>

<!-- business card: company back -->
<section class="sheet card-c" aria-label="Business card back">
  <svg class="bars" width="224" height="131" viewBox="0 0 224 131" aria-hidden="true">
    <polygon points="0,95 153,95 163,115 0,115" fill="var(--navy)"/>
    <polygon points="193,95 224,95 224,115 183,115" fill="var(--orange)"/>
  </svg>
  <div class="brand"><span class="dot"></span>VELTA HOME</div>
  <div class="company" style="top:48px">Velta Home srl</div>
  <div class="company" style="top:58px">Società unipersonale-Einzelunternehmen</div>
  <div class="line" style="top:87px">Via dei Pini - Pinienweg 8</div>
  <div class="line on-navy" style="top:97px">I-39012 Merano-Meran (Bz)</div>
  <div class="line on-navy" style="top:107px">REA - VWV Nr. Bz 731205</div>
  <div class="line" style="top:117px">P.I. - MWSt. 04812660215</div>
</section>

<!-- envelope -->
<section class="sheet envelope" aria-label="Envelope">
  <div class="watermark" aria-hidden="true"></div>
  <svg class="bars" width="582" height="271" viewBox="0 0 582 271" aria-hidden="true">
    <rect x="-6" y="131" width="61" height="11" rx="5.5" fill="var(--navy)"/>
    <rect x="-6" y="149" width="61" height="11" rx="5.5" fill="var(--navy)"/>
    <rect x="-6" y="166" width="61" height="11" rx="5.5" fill="var(--navy)"/>
    <rect x="-6" y="184" width="61" height="11" rx="5.5" fill="var(--navy)"/>
    <rect x="-6" y="202" width="61" height="11" rx="5.5" fill="var(--navy)"/>
    <polygon points="0,227 453,227 444,244 0,244" fill="var(--orange)"/>
    <polygon points="458,227 504,227 496,244 450,244" fill="var(--navy)"/>
    <polygon points="514,227 582,227 582,244 506,244" fill="var(--green)"/>
  </svg>
  <div class="brand"><span class="dot"></span>VELTA HOME</div>
  <div class="line" style="top:130px">+39 331 5208147</div>
  <div class="line" style="top:148px">office@velta-home.srl</div>
  <div class="line" style="top:165px">www.velta-home.srl</div>
  <div class="line" style="top:183px">info.veltahome@pec.it</div>
  <div class="line" style="top:201px">K7QWT42</div>
</section>

<!-- letterhead -->
<section class="sheet letterhead" aria-label="A4 letterhead">
  <div class="watermark" aria-hidden="true"></div>
  <svg class="bars" width="513" height="725" viewBox="0 0 513 725" aria-hidden="true">
    <polygon points="0,80 400,80 395,86 0,86" fill="var(--navy)"/>
    <polygon points="404,80 445,80 440,86 399,86" fill="var(--orange)"/>
    <polygon points="449,80 513,80 513,86 444,86" fill="var(--green)"/>
    <rect x="0" y="654" width="13" height="10" fill="var(--navy)"/>
    <polygon points="98,653 400,653 394,664 98,664" fill="var(--navy)"/>
    <polygon points="344,687 435,687 426,699 335,699" fill="var(--orange)"/>
    <polygon points="444,687 513,687 513,699 435,699" fill="var(--green)"/>
  </svg>

  <div class="brand head-brand"><span class="dot"></span>VELTA HOME</div>
  <div class="services">CLEANING · GARDENING · PESTCONTROL</div>

  <div class="line contact" style="top:32px"><span class="ico">
    <svg width="8" height="8" viewBox="0 0 10 10"><path d="M2 0l2 2-1 2 3 3 2-1 2 2-2 2C4 10 0 6 0 2z" fill="var(--ink)"/></svg></span>+39 331 5208147</div>
  <div class="line contact" style="top:47px"><span class="ico">
    <svg width="16" height="8" viewBox="0 0 16 8"><rect x=".5" y=".5" width="15" height="7" rx="3.5" fill="none" stroke="var(--ink)"/></svg></span>info.veltahome@pec.it</div>
  <div class="line contact" style="top:62px"><span class="ico">
    <svg width="8" height="10" viewBox="0 0 8 10"><rect x=".5" y=".5" width="7" height="9" fill="none" stroke="var(--ink)"/><path d="M2 4h4M2 6h4" stroke="var(--ink)"/></svg></span>K7QWT42</div>

  <div class="to">To,<strong>Mr. Rossi</strong></div>

  <p class="body" style="top:190px">Lorem ipsum dolor sit amet, consectetur adipiscing elit, sed do eiusmod tempor incididunt ut labore et dolore magna aliqua. Ut enim ad minim veniam, quis nostrud exercitation ullamco laboris nisi ut aliquip ex ea commodo consequat. Duis aute irure dolor in reprehenderit in voluptate velit esse cillum dolore eu fugiat nulla pariatur. Excepteur sint occaecat cupidatat non proident, sunt in culpa qui officia deserunt mollit anim id est laborum. Lorem ipsum dolor sit amet, consectetur adipiscing elit, sed do eiusmod tempor incididunt ut labore et dolore magna aliqua. Ut enim ad minim veniam, quis nostrud exercitation ullamco laboris nisi ut aliquip ex ea commodo consequat.</p>
  <p class="body" style="top:284px">Lorem ipsum dolor sit amet, consectetur adipiscing elit, sed do eiusmod tempor incididunt ut labore et dolore magna aliqua. Ut enim ad minim veniam, quis nostrud exercitation ullamco laboris nisi ut aliquip ex ea commodo consequat. Duis aute irure dolor in reprehenderit in voluptate velit esse cillum dolore eu fugiat nulla pariatur. Excepteur sint occaecat cupidatat non proident, sunt in culpa qui officia deserunt.</p>
  <p class="body" style="top:353px">Lorem ipsum dolor sit amet, consectetur adipiscing elit, sed do eiusmod tempor incididunt ut labore et dolore magna aliqua. Ut enim ad minim veniam, quis nostrud exercitation ullamco laboris nisi ut aliquip ex ea commodo consequat. Duis aute irure dolor in reprehenderit in voluptate velit esse cillum dolore eu fugiat nulla pariatur. Excepteur sint occaecat cupidatat non proident, sunt in culpa qui officia deserunt.</p>
  <p class="body" style="top:424px">Lorem ipsum dolor sit amet, consectetur adipiscing elit, sed do eiusmod tempor incididunt ut labore et dolore magna aliqua. Ut enim ad minim veniam, quis nostrud exercitation ullamco laboris nisi ut aliquip ex ea commodo consequat. Duis aute irure dolor in reprehenderit in voluptate velit esse cillum dolore eu fugiat nulla pariatur. Excepteur sint occaecat cupidatat non proident, sunt in culpa qui officia deserunt mollit anim id est laborum. Lorem ipsum dolor sit amet, consectetur adipiscing elit, sed do eiusmod tempor incididunt ut labore et dolore magna aliqua. Ut enim ad minim veniam, quis nostrud exercitation ullamco laboris nisi ut aliquip ex ea commodo consequat. Lorem ipsum dolor sit amet, consectetur adipiscing elit, sed do eiusmod tempor incididunt ut labore et dolore magna aliqua. Ut enim ad minim veniam, quis nostrud exercitation ullamco laboris nisi ut aliquip ex ea commodo consequat. Duis aute irure dolor in reprehenderit in voluptate velit esse cillum dolore eu fugiat nulla pariatur. Excepteur sint occaecat cupidatat non proident, sunt in culpa.</p>

  <div class="sign"><strong>Mr. Bauer</strong>Manager</div>

  <div class="brand foot-brand"><span class="dot"></span>VELTA HOME</div>
  <div class="line foot" style="left:143px"><span style="font-weight:700;margin-right:8px">@</span>office@velta-home.srl</div>
  <div class="line foot" style="left:272px"><span class="ico" style="margin-right:8px">
    <svg width="9" height="9" viewBox="0 0 10 10"><circle cx="5" cy="5" r="4.3" fill="none" stroke="var(--ink)"/><path d="M1 5h8M5 1v8" stroke="var(--ink)" stroke-width=".8"/></svg></span>www.velta-home.srl</div>
</section>

</body>
</html>
```